Brand Identity Poster - Sabor Ventana

We have a restaurant in Singapore - and looking for a graphic design on a poster - which we can use for all event signage. Our intent is to use this graphic design as a branding mechanism - that whenever the customer sees the image - they know it is Sabor Ventana.

The first photo below is one we found - that we love the combination of the feeling of the poster and the colors. Something similar to this is what we want.

The second file is our new logo.

The third and fourth files show pictures of the restaurant.

The image we wish to convey is relaxed dining - comfortable - and festive. We host a lot of events in the restaurant and we want to be the go-to place for families. We can handle up to 100 people in our restaurant - including outdoor space. Therefore many families and companies hold their gathering here.

Our food is fresh, cooked from the heart and is Filipino and Spanish Fusion. This cuisine includes a lot of seafood and pork.

We offer a great selection of tapas, wine and beer. As we are located in a Business Park, we will also use the image to announce our various "after work" specials so people can relax after hours - before going home.

In our logo - we are not entirely happy with the yellowish colors on the right side. If you have a different yellowish color that works well with the poster - then we are open to modifying the colors in the logo to better match the poster.

The last file is the AI file for the logo - in case you want to modify the colors.

We will make our decision quickly - hence this is a 5 day project.

Good luck and we look forward to your wonderful design ideas.

Project Deadline Extended Reason: Give designers time to adjust their designs based on the feedback given. Added Thursday, June 2, 2016

Hi Designers - we've been very busy in the last 2 days with the final construction of the relaunch. Posting new pictures of the decor, so you can do final design and color tweaks to match. Many thanks for all your great ideas. Added Wednesday, June 8, 2016

Target Market(s)

25 - 40 - Professionals (for professionals during lunch as this is a business park) and Families (for events on evenings and week-ends).

Industry/Entity Type

Restaurant

Requirements
Must have
• Must incorporate our logo - again open to changes in color of the logo - if that works better for you.
• Needs to match our "ventana" name.
• Works well with tapas and wine crowd.
• Have a clearly defined space on the poster - where we can announce different events, as this design will be reused on all events we host.
Nice to have
• The font should be complementary to the font in our logo name. Does not have to be identical - but looks well with the name.
Should not have
• Should not be child-like - as that is too specific of a market.

```html
<!DOCTYPE html>
<html lang="en">
<head>
<meta charset="utf-8">
<title>Sabor Ventana – Event Poster</title>
<link rel="stylesheet" href="https://fonts.googleapis.com/css2?family=Raleway:wght@600&display=swap">
<style>
  :root {
    --blue-deep: #4a74d0;
    --blue-sky: #6cbcec;
    --teal: #40b4b4;
    --orange: #ff7a38;
    --yellow: #ffe94f;
    --mist: #ebebeb;
    --white: #ffffff;
    --tagline: #3f6fd0;
  }
  html, body {
    margin: 0;
    padding: 0;
    overflow: hidden;
    background: #f4f4f4;
  }
  .poster {
    position: relative;
    width: 848px;
    height: 1200px;
    overflow: hidden;
    background: var(--blue-deep);
    font-family: "Raleway", Arial, sans-serif;
  }
  .foliage {
    position: absolute;
  }

  /* top edge */
  .foliage--mist-top      { left: 130px; top: -20px; width: 190px; height: 150px; background: var(--mist); border-radius: 0 0 50% 40%; }
  .foliage--hibiscus      { left: -30px; top: -30px; width: 300px; height: 360px; background: var(--orange); border-radius: 30% 40% 55% 45% / 30% 45% 60% 50%; }
  .foliage--fronds-top    { left: 270px; top: -30px; width: 230px; height: 270px; background: var(--blue-sky); border-radius: 40% 40% 50% 50% / 30% 30% 70% 70%; }
  .foliage--accents-top   { left: 410px; top: 14px; width: 170px; height: 80px; background: var(--orange); border-radius: 40px; transform: rotate(8deg); }
  .foliage--monstera      { left: 500px; top: -40px; width: 380px; height: 320px; background: var(--teal); border-radius: 45% 20% 40% 55% / 40% 20% 60% 60%; }

  /* left edge */
  .foliage--mist-left     { left: -30px; top: 190px; width: 130px; height: 210px; background: var(--mist); border-radius: 0 50% 50% 0; }
  .foliage--fern-left     { left: -20px; top: 230px; width: 250px; height: 270px; background: var(--teal); border-radius: 20% 60% 60% 20% / 30% 50% 60% 40%; }
  .foliage--palm-left     { left: -30px; top: 450px; width: 200px; height: 390px; background: var(--yellow); border-radius: 20% 70% 40% 30% / 30% 60% 40% 50%; }
  .foliage--accents-left  { left: 52px; top: 516px; width: 80px; height: 150px; background: var(--orange); border-radius: 40px; }
  .foliage--leaf-left     { left: -40px; top: 850px; width: 310px; height: 380px; background: var(--blue-sky); border-radius: 50% 60% 20% 20% / 40% 50% 20% 20%; }

  /* right edge */
  .foliage--palm-right    { left: 540px; top: 256px; width: 340px; height: 300px; background: var(--yellow); border-radius: 60% 10% 10% 60% / 50% 10% 10% 50%; }
  .foliage--mist-right    { left: 690px; top: 400px; width: 190px; height: 170px; background: var(--mist); border-radius: 50% 0 0 50%; }
  .foliage--leaf-right    { left: 680px; top: 620px; width: 200px; height: 270px; background: var(--blue-sky); border-radius: 60% 20% 20% 60% / 40% 20% 20% 60%; }

  /* bottom edge */
  .foliage--fronds-bottom { left: 464px; top: 824px; width: 420px; height: 400px; background: var(--blue-sky); border-radius: 50% 30% 0 0 / 40% 30% 0 0; }
  .foliage--mist-bottom   { left: 296px; top: 1024px; width: 500px; height: 220px; background: var(--mist); border-radius: 50% 50% 0 0 / 60% 60% 0 0; }
  .foliage--seaweed       { left: 336px; top: 848px; width: 240px; height: 370px; background: var(--teal); border-radius: 60% 60% 20% 20% / 50% 50% 10% 10%; }
  .foliage--berries       { left: 420px; top: 990px; width: 150px; height: 170px; background: var(--orange); border-radius: 50%; }

  .diners {
    position: absolute;
    background: var(--blue-sky);
    border-radius: 50%;
  }
  .diners--standing { left: 704px; top: 536px; width: 130px; height: 190px; background: var(--blue-deep); border-radius: 30% 30% 50% 50%; }
  .diners--seated   { left: 40px; top: 912px; width: 180px; height: 190px; background: #5aa3dc; border-radius: 30% 30% 45% 45%; }

  .event-panel {
    position: absolute;
    left: 166px;
    top: 204px;
    width: 514px;
    height: 794px;
    background: var(--white);
  }
  .brand {
    position: absolute;
    left: 0;
    top: 136px;
    width: 484px;
    text-align: center;
  }
  .brand__name {
    display: inline-flex;
    align-items: center;
    gap: 10px;
    margin: 0;
    font-size: 38px;
    line-height: 44px;
    font-weight: 600;
    color: var(--orange);
    letter-spacing: 0.5px;
  }
  .brand__dot {
    width: 14px;
    height: 14px;
    border-radius: 50%;
    background: var(--orange);
  }
  .brand__tagline {
    margin: 14px 0 0;
    font-size: 12px;
    line-height: 14px;
    font-weight: 600;
    letter-spacing: 0.4px;
    color: var(--tagline);
  }
</style>
</head>
<body>
  <main class="poster">
    <div class="foliage foliage--mist-top" role="img" aria-label="Pale grey leaf shape behind the flower"></div>
    <div class="foliage foliage--hibiscus" role="img" aria-label="Large orange tropical flower with yellow speckles"></div>
    <div class="foliage foliage--fronds-top" role="img" aria-label="Sky blue palm fronds"></div>
    <div class="foliage foliage--accents-top" role="img" aria-label="Orange brush-stroke accents"></div>
    <div class="foliage foliage--monstera" role="img" aria-label="Teal monstera leaf with yellow veins"></div>

    <div class="foliage foliage--mist-left" role="img" aria-label="Pale grey leaf shape"></div>
    <div class="foliage foliage--fern-left" role="img" aria-label="Teal fern branch"></div>
    <div class="foliage foliage--palm-left" role="img" aria-label="Yellow palm fronds"></div>
    <div class="foliage foliage--accents-left" role="img" aria-label="Orange brush-stroke accents"></div>
    <div class="foliage foliage--leaf-left" role="img" aria-label="Sky blue leaf with yellow dots"></div>

    <div class="foliage foliage--palm-right" role="img" aria-label="Bright yellow palm fronds"></div>
    <div class="foliage foliage--mist-right" role="img" aria-label="Pale grey leaf shape"></div>
    <div class="foliage foliage--leaf-right" role="img" aria-label="Sky blue leaf with yellow dots"></div>

    <div class="foliage foliage--fronds-bottom" role="img" aria-label="Sky blue fern fronds"></div>
    <div class="foliage foliage--mist-bottom" role="img" aria-label="Pale grey leaf shape"></div>
    <div class="foliage foliage--seaweed" role="img" aria-label="Teal seaweed-like leaves"></div>
    <div class="foliage foliage--berries" role="img" aria-label="Orange berries among the leaves"></div>

    <div class="diners diners--standing" role="img" aria-label="Two guests chatting over drinks at a standing table"></div>
    <div class="diners diners--seated" role="img" aria-label="A couple sharing drinks at a round yellow table"></div>

    <section class="event-panel">
      <header class="brand">
        <h1 class="brand__name"><span class="brand__dot"></span>Sabor Ventana</h1>
        <p class="brand__tagline">SPANISH FILIPINO FUSION</p>
      </header>
    </section>
  </main>
</body>
</html>
```